Nu-Disco track "Keep Turning Around" CD artwork.

Need cover art for the single entitled:
'Keep Turning Around'
Band: GlowPavlane
https://www.glimmerbook.example/pages/GlowPavlane/581036294417853
Here's the track:
http://tnq.example/48PzRuK
CD cover Inspiration for these disco inspired track is original LP art from Velvet Orbit Parade. GlowPavlane in place of VOP at top, include a disco ball, track title.
I'm envisioning "hipsters" dancing on the dancefloor....
Design will need to incorporate standard elements from the Brightmoor Platter label (PSD included)
Updates
Please READ the design brief. Otherwise what's the point of me writing it.
Artwork needs EP added at the end of the song title. "Keep Turning Around EP"
Hi folks.....song title has been shortened to make layouts easier. Eliminate "IT" from title. Title now "Keep Turning Round"
Reminder....the title is "Keep Turning Round EP"

```html
<!DOCTYPE html>
<html lang="en">
<head>
<meta charset="utf-8">
<title>GlowPavlane – Keep Turning Round EP</title>
<link rel="stylesheet" href="https://fonts.googleapis.com/css2?family=Audiowide&family=Berkshire+Swash&family=Abril+Fatface&display=swap">
<style>
  :root {
    --page: #f1f1f1;
    --night: #000000;
    --chrome: #e6e6e6;
    --chrome-edge: #5a5a5a;
    --glow-blue: #2f7bff;
    --glow-pink: #e43fd4;
    --floor-cyan: #3fd6e0;
    --floor-violet: #8a3cc4;
    --floor-magenta: #c4369a;
    --badge-blue: #1ea0cf;
    --label-ink: #0d0d0d;
    --label-square: #1f9ec9;
  }
  html, body {
    margin: 0;
    width: 1200px;
    height: 1000px;
    overflow: hidden;
    background: var(--page);
  }
  .cover {
    position: absolute;
    left: 230px;
    top: 137px;
    width: 742px;
    height: 742px;
    background: var(--night);
    overflow: hidden;
  }
  .disco-ball {
    position: absolute;
    left: 130px;
    top: -40px;
    width: 340px;
    height: 340px;
    border-radius: 50%;
    background:
      radial-gradient(circle at 50% 50%, #e8f2ff 0 18%, #8fb6e6 30%, #4a6fb8 40%, rgba(160,70,220,0.7) 50%, rgba(40,90,255,0.35) 62%, rgba(0,0,0,0) 72%);
  }
  .band-name {
    position: absolute;
    left: 0;
    width: 100%;
    top: 138px;
    margin: 0;
    text-align: center;
    font-family: "Audiowide", sans-serif;
    font-size: 62px;
    font-weight: 400;
    letter-spacing: 1px;
    color: var(--chrome);
    -webkit-text-stroke: 2px var(--chrome-edge);
    text-shadow: 0 2px 6px rgba(0,0,0,0.8);
    text-transform: uppercase;
  }
  .title {
    position: absolute;
    left: 0;
    width: 100%;
    top: 422px;
    margin: 0;
    text-align: center;
    white-space: nowrap;
    color: var(--chrome);
    -webkit-text-stroke: 1.5px #3a3a3a;
    text-shadow: 0 2px 4px rgba(0,0,0,0.9);
  }
  .title-script {
    font-family: "Berkshire Swash", cursive;
    font-size: 44px;
    font-weight: 400;
  }
  .title-ep {
    font-family: "Abril Fatface", serif;
    font-size: 40px;
    margin-left: 6px;
  }
  .dance-floor {
    position: absolute;
    left: 0;
    top: 470px;
    width: 742px;
    height: 272px;
    background:
      linear-gradient(180deg, rgba(0,0,0,0) 0%, rgba(0,0,0,0) 28%, var(--floor-cyan) 42%, #5aa9e6 62%, var(--floor-violet) 82%, var(--floor-magenta) 100%),
      linear-gradient(90deg, #2ab84a 0%, var(--floor-violet) 45%, #e62a7a 80%, #e0202a 100%);
  }
  .badge {
    position: absolute;
    right: 0;
    bottom: 0;
    width: 210px;
    height: 190px;
  }
  .label {
    position: absolute;
    left: 16px;
    bottom: 22px;
    display: flex;
    align-items: center;
    gap: 8px;
    font-family: "Audiowide", sans-serif;
    font-size: 15px;
    color: var(--label-ink);
  }
  .label-square {
    width: 70px;
    height: 80px;
    background: var(--label-square);
  }
</style>
</head>
<body>
  <main class="cover">
    <div class="disco-ball" role="img" aria-label="Glowing mirrored disco ball with rainbow light rays"></div>
    <h1 class="band-name">GlowPavlane</h1>
    <div class="dance-floor" role="img" aria-label="Lit disco dance floor in cyan, violet and magenta tiles with coloured laser beams"></div>
    <h2 class="title"><span class="title-script">Keep Turning Round</span><span class="title-ep">EP</span></h2>
    <svg class="badge" viewBox="0 0 210 190" aria-hidden="true">
      <polygon points="60,10 150,0 210,30 210,190 0,190 20,60" fill="var(--badge-blue)"/>
    </svg>
    <div class="label">
      <span class="label-square"></span>
      <span class="label-name">Brightmoor Platter</span>
    </div>
  </main>
</body>
</html>
```